Basic Website Design for Healthcare Services Startup

We need a professional designer to take our existing basic mobile website and create professional mobile and desktop website designs. We need the designer to use the existing content and page structure at our current mobile website (http://www.valtrix.com/phone/index.html) for the new design. Let us know if you have suggestions on how we can improve the site map.

The design needs to feel contemporary and clean. We need to convey a very professional operation that embraces technology. PLEASE refer to the attached brochure to understand the style and feel we want the website to have.

We want to start small and quickly iterate to a larger, final product. Initial submissions should only include a desktop homepage and a mobile homepage. I WILL PROVIDE INITIAL FEEDBACK AND COMMIT MONEY TO THE PROJECT BEFORE ASKING DESIGNERS TO COMPLETE A FULL DESIGN FOR THE ENTIRE DESKTOP AND MOBILE SITE.

We are happy to email you any stock photos you see on our current site. Please feel free to ask questions.

Please stay close to our current color scheme, but feel free to add new colors to our palette as needed.
Our blue is: #7CD9DA
Our gray is: #585751

Thanks Designers!!

Target Market(s)

Males, Ages 18-24

Industry/Entity Type

Health Care

Number of Pages Required

5+ page

Font styles to use
Sans Serif

Requirements
Must have
• -Final design must contain all content on www.valtrix.com/phone/ website.
• -All graphics/designs/content must be easily accessible in the final deliverable so we can import it into Adobe Muse for development.
• -Must be designed in Adobe.
• -Please specify different states: normal, rollover, active, etc.
• ***UPDATE***
• Thank you everyone for your submissions! I am very happy with the quality of submissions so I will commit to the guarantee. Please focus on my comments and submit your best 2 or 3 designers. I want to give strong feedback to all designers and it is difficult when there are many different combinations of the same design elements.
• A few quick notes to help guide future submissions:
• 1.) PICTURE CONTENT: right now the focus is on designing the landing page for our donors, so the audience is 18-24 males. We want a few medical pictures, but we mostly want to connect with our donor base. Please save the pictures of doctors for the HOSPITAL PAGE. For this main page we either want to see black or hispanic people donating blood, having fun, or being with friends and loved ones.
• 2.) HOMEPAGE CONTENT: Please use the content on www.valtrix.com/phone/index.html for homepage content guidance. We do not want to include a lot of the hospital brochure content on the homepage we want that content on the HOSPITAL PAGE).
• 3.) BLOG CONTENT: Add a section for articles/blog content. We want to feature the most recent post and small previews of the previous 2 or 3 articles.
• 4.) SOCIAL: we want our social media icons to be prominent. Either in the header or at the top of the page.
• 5.) NO PARTNERS: we don't want to include our partners on the donor homepage.
• ***UPDATE***
• Hi everyone, quick clarification. The final winner will need to include all these pages. Most of them should be very quick because they do not have a lot of content on them. Please focus on the donor homepage. I will approve the look and feel before asking you to create the rest of the pages. Please note I need both Desktop and
• Mobile versions of these designs:
• Pages Needed in final design:
• -Homepage <= 85% of design work should be on this page
• -Registration
• -Hospital
• -Donor Eligibility
• -How Valtrix Works
• -Learn About PBSC Donation
• -Learn About Blood Cancer
• -About Us
Nice to have
• -Nice to have an idea how we can make your design responsive.
Should not have
• None.

```html
<!DOCTYPE html>
<html lang="en">
<head>
<meta charset="utf-8">
<title>Valtrix – Donate Blood Stem Cells</title>
<link rel="stylesheet" href="https://fonts.googleapis.com/css2?family=Oswald:wght@400;500&family=Open+Sans:wght@400;600&display=swap">
<style>
:root{
  --blue:#7CD9DA;
  --gray:#585751;
  --ink:#3f3e3a;
  --panel:#f2f2f2;
  --footer:#efefef;
  --bar:#45443f;
  --white:#ffffff;
  --red:#e0261f;
}
*{margin:0;padding:0;box-sizing:border-box}
html,body{width:1200px;height:3175px;overflow:hidden;background:var(--white)}
body{position:relative;font-family:'Open Sans',sans-serif;color:var(--ink)}
.abs{position:absolute}
h1,h2,h3{font-weight:400}
.heading{font-family:'Oswald',sans-serif;font-weight:400;color:var(--ink);text-align:center;font-size:27px;letter-spacing:.2px}
.accent{color:var(--blue)}
.btn{position:absolute;display:flex;align-items:center;justify-content:center;font-family:'Oswald',sans-serif;font-size:18px;letter-spacing:.5px;color:var(--white);background:var(--blue);border-radius:3px;text-transform:uppercase}
.btn.dark{background:var(--gray)}

/* header */
.site-header{top:0;left:0;width:1200px;height:138px;background:var(--white)}
.brand-name{left:99px;top:28px;font-family:'Oswald',sans-serif;font-weight:500;font-size:36px;color:var(--gray)}
.nav{left:380px;top:94px;display:flex;gap:34px;font-family:'Oswald',sans-serif;font-size:14.5px;color:var(--ink);text-transform:uppercase;letter-spacing:.2px}
.social{top:36px;left:978px;display:flex;gap:14px}
.social span{width:32px;height:32px;border-radius:50%;background:var(--blue)}

/* hero */
.hero{top:138px;left:0;width:1200px;height:556px;background:linear-gradient(180deg,#8ec3ea 0%,#b6d9f1 52%,#7aa9c6 70%,#d9cbb7 100%)}
.hero-people{top:138px;left:530px;width:670px;height:556px;background:linear-gradient(100deg,rgba(120,80,60,0) 0%,rgba(140,95,70,.55) 25%,rgba(90,100,150,.65) 70%,rgba(90,100,150,.4) 100%)}
.hero-circle{left:86px;top:205px;width:424px;height:424px;border-radius:50%;border:2px solid #5f6a70;background:rgba(255,255,255,.35);text-align:center}
.hero-title{margin-top:82px;font-family:'Oswald',sans-serif;font-weight:400;font-size:46px;line-height:54px;color:#2f2f2c;letter-spacing:.5px}
.hero-title b{font-weight:500}
.hero-copy{margin:22px auto 0;width:300px;font-size:17px;line-height:26px;color:#333}
.hero-circle .btn{left:99px;top:286px;width:226px;height:42px;background:#4c4b47}
.hero-dots{position:absolute;left:182px;top:364px;display:flex;gap:12px}
.hero-dots span{width:13px;height:13px;border-radius:50%;background:#9aa3a8}
.hero-dots span.on{background:#4d5357}

/* video */
.video-heading{top:730px;left:0;width:1200px}
.video{left:345px;top:810px;width:510px;height:305px;border-radius:8px;border:3px solid #d8d8d8;overflow:hidden;background:#1e1e1e}
.video-frame{left:0;top:0;width:504px;height:250px;background:linear-gradient(120deg,#3b3a44 0%,#6b5a52 40%,#8a8f9a 70%,#4a4b55 100%)}
.play{left:222px;top:95px;width:58px;height:58px;border-radius:50%;background:var(--white)}
.controls{left:0;top:250px;width:504px;height:49px;background:#111;color:var(--white);font-size:14px;display:flex;align-items:center;padding:0 14px;gap:14px}
.track{width:280px;height:10px;background:#555;border-radius:5px;position:relative}
.track i{position:absolute;left:0;top:0;width:100px;height:10px;background:var(--red);border-radius:5px}
.track b{position:absolute;left:92px;top:-4px;width:18px;height:18px;border-radius:50%;background:#eee}

/* needed */
.needed{top:1168px;left:0;width:1200px;height:313px;background:var(--panel)}
.needed-heading{top:1202px;left:0;width:1200px}
.facts{font-size:14.5px;line-height:22px;color:var(--ink)}
.fact{position:absolute;display:flex;gap:14px;align-items:flex-start;width:440px}
.fact svg{flex:none;margin-top:-2px}

/* blog */
.blog-title{font-family:'Oswald',sans-serif;font-weight:400;font-size:29px;color:var(--ink)}
.card{border:1px solid #dcdcdc;background:var(--white);box-shadow:0 1px 3px rgba(0,0,0,.08)}
.card-title{font-family:'Oswald',sans-serif;font-weight:500;font-size:15px;color:var(--ink);text-decoration:underline}
.card-date{font-size:12px;color:var(--blue);margin:6px 0 6px}
.card-text{font-size:12.5px;line-height:20px;color:#555}
.card-text a{color:var(--blue)}
.thumbs{display:flex;gap:6px}
.thumbs span{width:44px;height:34px;background:linear-gradient(135deg,#4d3b33,#8a7566)}

/* how it works */
.how{top:1879px;left:0;width:1200px;height:413px;background:var(--panel)}
.step{position:absolute;width:240px;text-align:center}
.step-icon{width:76px;height:76px;border-radius:50%;background:var(--blue);margin:0 auto;display:flex;align-items:center;justify-content:center}
.step-label{font-family:'Oswald',sans-serif;font-size:17px;margin-top:18px;color:var(--ink);text-transform:uppercase}
.step-text{font-size:13.5px;line-height:22px;font-weight:600;margin-top:8px;color:#333}
.connector{position:absolute;display:flex;gap:14px;align-items:center}
.connector span{border-radius:50%;background:#dcdcdc}

/* testimonials */
.avatar{left:95px;top:2414px;width:138px;height:138px;border-radius:50%;border:5px solid var(--blue);background:linear-gradient(160deg,#eae6e2,#c7b9ac)}
.quote-mark{left:285px;top:2404px;font-family:'Oswald',sans-serif;font-size:96px;line-height:1;color:#cfcfcf}
.quote{left:290px;top:2422px;width:820px;font-size:13.5px;line-height:27px;font-style:italic;color:#444;text-indent:64px}
.quote-rule{left:290px;top:2558px;width:812px;height:1px;background:#e3e3e3}
.quote-name{left:284px;top:2572px;font-size:13px;color:var(--blue)}
.dots{left:1046px;top:2540px;display:flex;gap:10px}
.dots span{width:10px;height:10px;border-radius:50%;background:#555}
.dots span.off{background:#c9c9c9}

/* split */
.split-left{top:2639px;left:0;width:600px;height:385px;background:var(--gray)}
.split-right{top:2639px;left:600px;width:600px;height:385px;background:var(--blue)}
.split-col{position:absolute;width:420px;text-align:center;color:var(--white)}
.split-title{font-family:'Oswald',sans-serif;font-weight:400;font-size:29px;margin-top:20px}
.split-text{font-size:13px;line-height:20px;margin:12px auto 0;width:310px}
.center-badge{left:523px;top:2783px;width:152px;height:95px;background:var(--white);border:3px solid #4d4c48;border-radius:6px;display:flex;align-items:center;justify-content:center;font-family:'Oswald',sans-serif;font-weight:500;font-size:24px;color:var(--gray)}

/* footer */
.footer{top:3024px;left:0;width:1200px;height:99px;background:var(--footer)}
.footer-social{left:99px;top:3047px;display:flex;gap:22px}
.footer-social span{width:52px;height:52px;border-radius:50%;background:var(--blue)}
.bottom-bar{top:3123px;left:0;width:1200px;height:52px;background:var(--bar);color:#e8e8e8;font-size:11.5px;display:flex;align-items:center;justify-content:space-between;padding:0 99px}
.bottom-bar nav{display:flex;gap:8px}
</style>
</head>
<body>

<header class="abs site-header">
  <div class="abs brand-name">Valtrix</div>
  <div class="abs social"><span></span><span></span><span></span></div>
  <nav class="abs nav">
    <span>Hospital</span><span>How Valtrix Works</span><span>Registration</span><span>Learn About PBSC Donation</span><span>Learn About Blood Cancer</span>
  </nav>
</header>

<section>
  <div class="abs hero" role="img" aria-label="Photo of a smiling couple embracing by the sea under a blue sky"></div>
  <div class="abs hero-people" role="img" aria-label="Couple embracing, man in a blue t-shirt"></div>
  <div class="abs hero-circle">
    <h1 class="hero-title">DONATE BLOOD<br>EARN <b>$2,000</b></h1>
    <p class="hero-copy">Register to donate blood stem cells and join the fight against cancer!</p>
    <span class="btn">Register Today</span>
    <div class="hero-dots"><span></span><span class="on"></span><span></span></div>
  </div>
</section>

<section>
  <h2 class="abs heading video-heading">Learn More About Stem Cell Donations. <span class="accent">Watch Marcus Donate to Help a Little Girl!</span></h2>
  <div class="abs video">
    <div class="abs video-frame" role="img" aria-label="Video still of a donor seated in a clinic chair giving blood"></div>
    <div class="abs play"><svg width="58" height="58" viewBox="0 0 58 58"><path d="M23 18 L41 29 L23 40Z" fill="#222"/></svg></div>
    <div class="abs controls">
      <svg width="14" height="16" viewBox="0 0 14 16"><path d="M2 1 L13 8 L2 15Z" fill="#fff"/></svg>
      <span>04:59</span>
      <div class="track"><i></i><b></b></div>
      <span>10:35</span>
      <svg width="18" height="16" viewBox="0 0 18 16"><path d="M1 5h4l5-4v14l-5-4H1z" fill="#fff"/><path d="M13 4q3 4 0 8" stroke="#fff" fill="none" stroke-width="1.6"/></svg>
      <svg width="16" height="16" viewBox="0 0 16 16"><path d="M2 2l12 12M2 2h5M2 2v5M14 14H9M14 14V9" stroke="#fff" stroke-width="2" fill="none"/></svg>
    </div>
  </div>
</section>

<section>
  <div class="abs needed"></div>
  <h2 class="abs heading needed-heading">You are Desperately <span class="accent">Needed to Save a Life</span></h2>
  <div class="facts">
    <div class="fact" style="left:99px;top:1286px"><svg width="22" height="22" viewBox="0 0 22 22"><circle cx="11" cy="11" r="9" fill="none" stroke="#666" stroke-width="1.5"/><path d="M6 11l4 4 9-10" fill="none" stroke="#444" stroke-width="2"/></svg><span>1 in 3 minority blood cancer patients cannot find a donor</span></div>
    <div class="fact" style="left:99px;top:1341px"><svg width="22" height="22" viewBox="0 0 22 22"><circle cx="11" cy="11" r="9" fill="none" stroke="#666" stroke-width="1.5"/><path d="M6 11l4 4 9-10" fill="none" stroke="#444" stroke-width="2"/></svg><span>Matches usually occur between people of the same race</span></div>
    <div class="fact" style="left:99px;top:1396px"><svg width="22" height="22" viewBox="0 0 22 22"><circle cx="11" cy="11" r="9" fill="none" stroke="#666" stroke-width="1.5"/><path d="M6 11l4 4 9-10" fill="none" stroke="#444" stroke-width="2"/></svg><span>Valtrix recruits donors for African American, Asian, and Hispanic communities</span></div>
    <div class="fact" style="left:637px;top:1286px;width:480px"><svg width="22" height="22" viewBox="0 0 22 22"><circle cx="11" cy="11" r="9" fill="none" stroke="#666" stroke-width="1.5"/><path d="M6 11l4 4 9-10" fill="none" stroke="#444" stroke-width="2"/></svg><span>You might be the ONLY person that can save someone's life</span></div>
    <div class="fact" style="left:637px;top:1341px;width:480px"><svg width="22" height="22" viewBox="0 0 22 22"><circle cx="11" cy="11" r="9" fill="none" stroke="#666" stroke-width="1.5"/><path d="M6 11l4 4 9-10" fill="none" stroke="#444" stroke-width="2"/></svg><span>Over 8,000 Americans need a blood stem cell donation each year</span></div>
  </div>
  <span class="btn" style="left:643px;top:1397px;width:225px;height:44px">Register Today</span>
</section>

<section>
  <h2 class="abs blog-title" style="left:99px;top:1506px">Latest <span class="accent">Blog Posts</span></h2>
  <svg class="abs" style="left:556px;top:1520px" width="30" height="16" viewBox="0 0 30 16"><path d="M8 2 2 8l6 6M22 2l6 6-6 6" fill="none" stroke="#999" stroke-width="1.8"/></svg>
  <h2 class="abs blog-title" style="left:611px;top:1506px">Featured <span class="accent">Articles</span></h2>
  <span class="abs" style="left:1042px;top:1520px;font-size:14px;color:#b5b5b5">View All</span>

  <article class="abs card" style="left:99px;top:1576px;width:487px;height:235px">
    <div class="abs" style="left:7px;top:9px;width:203px;height:218px;background:linear-gradient(160deg,#c9d3dc,#8b9aa4 60%,#7a6a5c)" role="img" aria-label="Photo of a donor relaxing with headphones during blood stem cell collection"></div>
    <div class="abs" style="left:235px;top:20px;width:235px">
      <h3 class="card-title">Ut tellus dolor, dapibus smit dollar</h3>
      <p class="card-date">13Mar, 2016</p>
      <p class="card-text">Duis autem vel eum iriure dolor in hendrerit in vulputate velit esse molestie consequat, vel illum dolore eu feugiat nulla facilisis at vero eros et accumsan et iusto odio dignissim nulla facilisi. <a>[...]</a></p>
    </div>
  </article>

  <article class="abs card" style="left:611px;top:1576px;width:489px;height:235px">
    <div class="abs" style="left:8px;top:10px;width:199px;height:171px;background:linear-gradient(135deg,#6b4a38,#a27b5e 50%,#3b3434)" role="img" aria-label="Photo of a smiling man in a dark suit in front of a brick wall"></div>
    <div class="abs thumbs" style="left:8px;top:189px"><span></span><span></span><span></span><span></span></div>
    <div class="abs" style="left:218px;top:18px;width:258px">
      <h3 class="card-title">Lorem tellus dolor, dapibus smit dollar</h3>
      <p class="card-date">22March, 2016</p>
      <p class="card-text">Duis autem vel eum iriure dolor in hendrerit in vulputate velit esse molestie consequat, vel illum dolore eu feugiat nulla facilisis at vero eros et accumsan et iusto odio dignissim nulla facilisi. Duis autem vel eum iriure dolor in hendrerit in vulputate velit esse molestie consequat, vel illum dolore.</p>
    </div>
  </article>
</section>

<section>
  <div class="abs how"></div>
  <h2 class="abs heading" style="top:1915px;left:0;width:1200px">How <span class="accent">Valtrix Works</span></h2>

  <div class="connector" style="left:286px;top:2032px"><span style="width:8px;height:8px"></span><span style="width:10px;height:10px"></span><span style="width:12px;height:12px"></span><span style="width:14px;height:14px"></span><span style="width:16px;height:16px"></span></div>
  <div class="connector" style="left:540px;top:2032px"><span style="width:8px;height:8px"></span><span style="width:10px;height:10px"></span><span style="width:12px;height:12px"></span><span style="width:14px;height:14px"></span><span style="width:16px;height:16px"></span></div>
  <div class="connector" style="left:794px;top:2032px"><span style="width:8px;height:8px"></span><span style="width:10px;height:10px"></span><span style="width:12px;height:12px"></span><span style="width:14px;height:14px"></span><span style="width:16px;height:16px"></span></div>

  <div class="step" style="left:96px;top:1993px">
    <div class="step-icon"><svg width="34" height="40" viewBox="0 0 34 40"><rect x="3" y="5" width="28" height="33" rx="2" fill="none" stroke="#fff" stroke-width="2.5"/><rect x="11" y="1" width="12" height="7" rx="1" fill="#fff"/><path d="M9 16h16M9 22h16M9 28h12" stroke="#fff" stroke-width="2.5"/></svg></div>
    <div class="step-label">Swab</div>
    <p class="step-text">Lorem ipsum dolor sit amet, consectetuer adipiscing elit sed diamsit almet dolor</p>
  </div>
  <div class="step" style="left:350px;top:1993px">
    <div class="step-icon"><svg width="26" height="40" viewBox="0 0 26 40"><rect x="2" y="2" width="22" height="36" rx="3" fill="none" stroke="#fff" stroke-width="2.5"/><path d="M2 8h22M2 31h22" stroke="#fff" stroke-width="2"/><circle cx="13" cy="34.5" r="1.6" fill="#fff"/></svg></div>
    <div class="step-label">Contact</div>
    <p class="step-text">Lorem ipsum dolor sit amet, consectetuer adipiscing elit sed diamsit almet dolor</p>
  </div>
  <div class="step" style="left:604px;top:1993px">
    <div class="step-icon"><svg width="34" height="40" viewBox="0 0 34 40"><rect x="12" y="2" width="8" height="20" rx="1" fill="#fff" transform="rotate(-20 16 12)"/><path d="M6 36h24M10 36q-4-12 8-16" fill="none" stroke="#fff" stroke-width="3"/><rect x="9" y="30" width="16" height="4" fill="#fff"/></svg></div>
    <div class="step-label">Lab Testing</div>
    <p class="step-text">Lorem ipsum dolor sit amet, consectetuer adipiscing elit sed diamsit almet dolor</p>
  </div>
  <div class="step" style="left:860px;top:1993px">
    <div class="step-icon"><svg width="36" height="40" viewBox="0 0 36 40"><circle cx="18" cy="11" r="8" fill="#fff"/><path d="M3 38q0-16 15-16t15 16z" fill="#fff"/><path d="M18 24v8M14 28h8" stroke="#7CD9DA" stroke-width="2.5"/></svg></div>
    <div class="step-label">Medical Workup</div>
    <p class="step-text">Lorem ipsum dolor sit amet, consectetuer adipiscing elit sed diamsit almet dolor</p>
  </div>

  <span class="btn" style="left:512px;top:2218px;width:201px;height:42px">Register Today</span>
</section>

<section>
  <h2 class="abs heading" style="top:2340px;left:0;width:1200px">Client <span class="accent">Testimonials</span></h2>
  <div class="abs avatar" role="img" aria-label="Portrait photo of a client"></div>
  <div class="abs quote-mark">“</div>
  <p class="abs quote">Lorem ipsum dolor smit amet, consectetuer adipiscing elitmk, sed diamt diam nonummy nibh euismod tincidunt ut nt ut laoreetml dolore magna aliquam erat volutpat. Ut wisi enim ad minim veniam, quis nostrud exer tationk ullamcorper suscipit lobortisk nisl utml aliqpi ex ea commodo consequat. Duis autem vel eumk iriure dolor inj hendrerit inn vulputate velit esse molestiene consequat, velhki illumn gnol dolore eu feugiat nulla facilisis.</p>
  <div class="abs quote-rule"></div>
  <p class="abs quote-name">- Mr. Arlen Moss</p>
  <div class="abs dots" style="top:2568px"><span class="off"></span><span></span><span></span></div>
</section>

<section>
  <div class="abs split-left"></div>
  <div class="abs split-right"></div>

  <div class="split-col" style="left:90px;top:2700px">
    <svg width="70" height="60" viewBox="0 0 70 60"><circle cx="35" cy="14" r="10" fill="#fff"/><circle cx="14" cy="20" r="7" fill="#fff"/><circle cx="56" cy="20" r="7" fill="#fff"/><path d="M20 52q0-24 15-24t15 24z" fill="#fff"/><path d="M2 50q0-20 12-20 6 0 9 4-5 6-5 16z" fill="#fff"/><path d="M68 50q0-20-12-20-6 0-9 4 5 6 5 16z" fill="#fff"/></svg>
    <h3 class="split-title">Become A <span class="accent">H.E.R.O</span></h3>
    <p class="split-text">Lorem ipsum dolor sit amet, consectetuer adipiscing elit sed diamsit almet dolor Lorem ipsum dolor sit</p>
  </div>
  <span class="btn" style="left:214px;top:2931px;width:171px;height:42px">Organise Now</span>

  <div class="split-col" style="left:690px;top:2690px">
    <svg width="46" height="70" viewBox="0 0 46 70"><path d="M23 2C16 18 4 30 4 44a19 19 0 0 0 38 0C42 30 30 18 23 2z" fill="#fff"/><path d="M23 40v18M14 49h18" stroke="#7CD9DA" stroke-width="5"/></svg>
    <h3 class="split-title" style="margin-top:14px">Organize A <span style="color:var(--gray)">Donor Drive</span></h3>
    <p class="split-text">Lorem ipsum dolor sit amet, consectetuer adipiscing elit sed diamsit almet dolor Lorem ipsum dolor sit</p>
  </div>
  <span class="btn dark" style="left:813px;top:2931px;width:171px;height:42px">Contact Now</span>

  <div class="abs center-badge">Valtrix</div>
</section>

<footer>
  <div class="abs footer"></div>
  <div class="abs footer-social"><span></span><span></span><span></span></div>
  <span class="btn" style="left:887px;top:3051px;width:213px;height:42px">Register Today</span>
  <div class="abs bottom-bar">
    <nav><span>About Us</span><span>»</span><span>Donor Eligibility</span><span>»</span><span>Contact Us</span><span>»</span><span>Terms of Use</span><span>»</span><span>Legal and Privacy Policy</span></nav>
    <span>Copyright © 2016 - VALTRIX.  All Rights Reserved.</span>
  </div>
</footer>

</body>
</html>
```